MAPLEWREN HOUSE DECOR

We need a web design for a new business based in Wren Bay (NSW). We are a small retail outlet on the Saltwater Coast (Eastland Shore) selling home wares, gifts, beach wear, artwork, and hampers etc. We would like to a few different samples if that's not too much trouble (e.g. black and white vs colour, e.g. "beach colours").
We would like the website to communicate that we are an affordable, local (community based) business, with customer satisfaction at the forefront of our mind. We have a strong customer service focus, and in addition to retail sales we are now looking to expand into the online hamper business.
We are open 7 days (except public holidays).
Note: We like the design / layout of the "Lamp Crest 'N' Shelf Website" if you would like to compare www.lampcrestnshelf.com.au

```html
<!DOCTYPE html>
<html lang="en">
<head>
<meta charset="utf-8">
<title>Maplewren House Decor</title>
<link href="https://fonts.googleapis.com/css2?family=Lato:wght@400;700&family=Lora:ital@0;1&display=swap" rel="stylesheet">
<style>
:root{
  --backdrop:#f5ead0;
  --page:#ffffff;
  --ink:#2f2f2f;
  --muted:#6a6a6a;
  --tan:#c49a6c;
  --teal:#4eaaa8;
  --aqua:#7cc0c0;
  --line:#e3e3e3;
  --sans:'Lato', Arial, sans-serif;
  --serif:'Lora', Georgia, serif;
}
*{margin:0;padding:0;box-sizing:border-box}
html,body{width:1200px;height:2236px;overflow:hidden}
body{background:var(--backdrop);font-family:var(--sans);color:var(--ink);position:relative}
.page{position:absolute;left:121px;top:47px;width:960px;height:2142px;background:var(--page)}
.abs{position:absolute}

/* header */
.logo{left:24px;top:28px;width:33px;height:33px;background:var(--tan);color:#fff;font-size:8px;display:flex;align-items:center;justify-content:center}
.nav{top:38px;font-size:11px;color:var(--ink)}
.account{top:36px;font-size:11px;display:flex;align-items:center;gap:6px}
.search{left:902px;top:28px;width:32px;height:32px;border:1px solid #888;display:flex;align-items:center;justify-content:center}
.header-rule{left:24px;top:87px;width:910px;height:1px;background:var(--line)}

/* hero */
.hero-title{left:0;top:186px;width:960px;text-align:center;font-size:58px;letter-spacing:3px;font-weight:400}
.hero-sub{left:0;top:264px;width:960px;text-align:center;font-family:var(--serif);font-style:italic;font-size:20px;color:var(--muted)}
.btn{left:391px;top:340px;width:175px;height:45px;background:var(--tan);color:#fff;font-size:10px;letter-spacing:.5px;display:flex;align-items:center;justify-content:center}

/* feature grid */
.grid{left:24px;top:503px;width:909px;height:681px}
.tile{position:absolute;display:flex;flex-direction:column;align-items:center;justify-content:center;text-align:center;color:#fff}
.tile-name{font-weight:700;font-size:19px;line-height:1.15;letter-spacing:.5px}
.tile-note{font-family:var(--serif);font-style:italic;font-size:14px;margin-top:4px;letter-spacing:.5px}
.tile-arrow{font-size:24px;line-height:1;margin-bottom:4px}
.shade{text-shadow:0 1px 3px rgba(0,0,0,.35)}

/* sale */
.section-title{left:0;width:960px;text-align:center;font-size:30px;font-weight:700;letter-spacing:1px}
.show-more{left:0;top:1276px;width:960px;text-align:center;font-family:var(--serif);font-style:italic;font-size:14px;color:var(--muted)}
.show-more span{text-decoration:underline}
.product{top:1343px;width:196px}
.product-photo{width:196px;height:196px}
.product-name{margin-top:26px;text-align:center;font-size:11px;font-weight:700}
.product-price{margin-top:4px;text-align:center;font-size:11px;color:var(--muted)}

/* newsletter */
.news-sub{left:0;top:1698px;width:960px;text-align:center;font-family:var(--serif);font-style:italic;font-size:16px;color:var(--muted)}
.email{left:259px;top:1760px;width:368px;height:43px;border:1px solid #bbb;font-family:var(--serif);font-style:italic;font-size:11px;color:#888;padding-left:12px;display:flex;align-items:center}
.send{left:626px;top:1760px;width:73px;height:43px;background:var(--tan);color:#fff;font-size:11px;display:flex;align-items:center;justify-content:center}

/* strip */
.strip{left:24px;top:1857px;width:909px;height:89px;display:flex}
.strip div{flex:1}
.strip-arrow{top:1877px;width:22px;height:48px;background:rgba(255,255,255,.7);display:flex;align-items:center;justify-content:center}

/* footer */
.foot-col{top:2006px;width:200px;padding-left:10px}
.foot-col+.foot-col{border-left:1px solid var(--line)}
.foot-col h4{font-size:10px;font-weight:700;letter-spacing:1px;margin-bottom:10px}
.foot-col li{list-style:none;font-size:9.5px;color:var(--muted);line-height:18px}
.social{display:flex;gap:22px;margin-top:6px}
.social i{width:10px;height:10px;border-radius:50%;background:var(--tan);display:block}
</style>
</head>
<body>
<div class="page">
  <header>
    <div class="abs logo">LOGO</div>
    <nav>
      <span class="abs nav" style="left:103px">Homeware</span>
      <span class="abs nav" style="left:196px">Kitchesware</span>
      <span class="abs nav" style="left:298px">Linen</span>
      <span class="abs nav" style="left:362px">Gifts</span>
      <span class="abs nav" style="left:425px">About</span>
    </nav>
    <div class="abs account" style="left:688px">
      <svg width="10" height="12" viewBox="0 0 10 12"><circle cx="5" cy="3" r="2.8" fill="#222"/><path d="M0 12c0-4 2-5.5 5-5.5s5 1.5 5 5.5z" fill="#222"/></svg>My Account</div>
    <div class="abs account" style="left:794px">
      <svg width="11" height="12" viewBox="0 0 11 12"><path d="M3 4V3a2.5 2.5 0 0 1 5 0v1" fill="none" stroke="#222" stroke-width="1.2"/><rect x="0.5" y="4" width="10" height="8" fill="#222"/></svg>Basket (0)</div>
    <div class="abs search"><svg width="12" height="12" viewBox="0 0 12 12"><circle cx="4.8" cy="4.8" r="3.5" fill="none" stroke="#222" stroke-width="1.4"/><path d="M7.5 7.5L11 11" stroke="#222" stroke-width="1.6"/></svg></div>
    <div class="abs header-rule"></div>
  </header>

  <section class="hero">
    <h1 class="abs hero-title">MAPLEWREN HOUSE DECOR</h1>
    <p class="abs hero-sub">Quisque lorem tortor fringilla sed, vestibulum id, eleifend justo.</p>
    <div class="abs btn">CHECK NEW ARRIVALS</div>
  </section>

  <section class="abs grid">
    <div class="tile shade" role="img" aria-label="Stacked teal and red bamboo salad bowls on wooden table" style="left:0;top:0;width:227px;height:454px;background:linear-gradient(160deg,#7a8f80 0%,#b65a3c 45%,#8a5a34 75%,#6e4a2e 100%)">
      <div class="tile-name">BAMBOO<br>SALAD BOWL</div><div class="tile-note">NEW ARRIVAL</div></div>
    <div class="tile shade" role="img" aria-label="Teal antique alarm clock" style="left:227px;top:0;width:227px;height:227px;background:linear-gradient(160deg,#8b8784,#6e6a66 60%,#9a8670)">
      <div class="tile-name">ANTIQUE<br>CLOCK</div><div class="tile-note">$45.00</div></div>
    <div role="img" aria-label="Turquoise glass vases on a mosaic table" class="tile" style="left:454px;top:0;width:227px;height:227px;background:linear-gradient(180deg,#e9eceb 0%,#3cc6bb 50%,#2fa8a3 80%,#cfd7d5 100%)"></div>
    <div class="tile" style="left:681px;top:0;width:228px;height:227px;background:var(--aqua)">
      <div class="tile-arrow">&larr;</div><div class="tile-name">AQUA VASE</div><div class="tile-note">TROPICANA</div></div>

    <div class="tile" style="left:227px;top:227px;width:227px;height:227px;background:var(--teal)">
      <div class="tile-arrow">&rarr;</div><div class="tile-name">BYRON FRAMES</div><div class="tile-note">ROSEWOOD</div></div>
    <div role="img" aria-label="Orange rosewood picture frame with a house print" class="tile" style="left:454px;top:227px;width:227px;height:227px;background:radial-gradient(circle at 50% 50%,#f1ece2 20%,#e07a3a 38%,#b8b46a 60%,#8c9a6a 100%)"></div>
    <div class="tile shade" role="img" aria-label="Shop interior with shelves of cushions and homewares" style="left:681px;top:227px;width:228px;height:454px;background:linear-gradient(180deg,#6e6a5e 0%,#7c7a6e 40%,#8c8778 70%,#6a6356 100%)">
      <div class="tile-name">VISIT<br>OUR SHOP</div><div class="tile-note">WREN BAY</div></div>

    <div role="img" aria-label="Clear glass candlesticks with white candles" class="tile" style="left:0;top:454px;width:227px;height:227px;background:linear-gradient(180deg,#a9d8dc,#d8eef0 60%,#b8dcde)"></div>
    <div class="tile" style="left:227px;top:454px;width:227px;height:227px;background:var(--tan)">
      <div class="tile-arrow">&larr;</div><div class="tile-name">CANDLESTICKS</div><div class="tile-note">CLEAN GLASS</div></div>
    <div class="tile shade" role="img" aria-label="Bamboo bread tray with sliced loaf" style="left:454px;top:454px;width:227px;height:227px;background:linear-gradient(180deg,#8a7a66 0%,#a08668 45%,#b23a2e 85%,#7c6650 100%)">
      <div class="tile-name">BAMBOO<br>BREAD TRAY</div><div class="tile-note">$65.00</div></div>
  </section>

  <section class="sale">
    <h2 class="abs section-title" style="top:1230px">ON SALE</h2>
    <p class="abs show-more"><span>show more</span> &rsaquo;</p>
    <div class="abs product" style="left:32px"><div class="product-photo" role="img" aria-label="Green jug, glasses and salad bowl" style="background:linear-gradient(150deg,#f0efe8,#6fae3a 50%,#8a6a48)"></div><p class="product-name">Miami Servingware</p><p class="product-price">$ 89.95</p></div>
    <div class="abs product" style="left:265px"><div class="product-photo" role="img" aria-label="Floral patterned tablecloth on a table" style="background:linear-gradient(180deg,#e6e2dc,#d98a6a 50%,#c45a4a 75%,#8a7e74)"></div><p class="product-name">Baman Tablecloth</p><p class="product-price">$ 59.95</p></div>
    <div class="abs product" style="left:499px"><div class="product-photo" role="img" aria-label="Blue and white chevron cushions" style="background:linear-gradient(135deg,#2a4a8a,#4a9ad8 45%,#e8eef4 70%,#3a80c8)"></div><p class="product-name">Chevron Cushion</p><p class="product-price">$ 99.95</p></div>
    <div class="abs product" style="left:732px"><div class="product-photo" role="img" aria-label="Rope lantern and birdcage jar" style="background:linear-gradient(180deg,#f2f2f0,#cdbca0 55%,#9a7e5a 80%,#e8e6e2)"></div><p class="product-name">Lantern Rope Jar</p><p class="product-price">$ 49.95</p></div>
  </section>

  <section class="news">
    <h2 class="abs section-title" style="top:1657px">BE THE FIRST TO KNOW</h2>
    <p class="abs news-sub">Nulla ipsum dolor lacus, suscipit adipiscing. Cum sociis natoque penatibus et ultrices volutpat.</p>
    <div class="abs email">Enter your email</div>
    <div class="abs send">SEND</div>
  </section>

  <div class="abs strip" role="img" aria-label="Row of product photos: clock, bread tray, vases, salad bowl, frame, lantern">
    <div style="background:linear-gradient(90deg,#cfd8d8,#6a9a9a)"></div>
    <div style="background:linear-gradient(90deg,#8a6a4a,#b84a34)"></div>
    <div style="background:linear-gradient(90deg,#e6e8e6,#3ab8b0)"></div>
    <div style="background:linear-gradient(90deg,#7ab0a8,#f2f0ea)"></div>
    <div style="background:linear-gradient(90deg,#e04a2e,#a07a50)"></div>
    <div style="background:linear-gradient(90deg,#b0b070,#e07a3a)"></div>
    <div style="background:linear-gradient(90deg,#c0ae90,#e8e6e2)"></div>
  </div>
  <div class="abs strip-arrow" style="left:24px"><svg width="8" height="14" viewBox="0 0 8 14"><path d="M7 1L1 7l6 6" fill="none" stroke="#fff" stroke-width="1.5"/></svg></div>
  <div class="abs strip-arrow" style="left:911px"><svg width="8" height="14" viewBox="0 0 8 14"><path d="M1 1l6 6-6 6" fill="none" stroke="#fff" stroke-width="1.5"/></svg></div>

  <footer>
    <div class="abs foot-col" style="left:257px"><h4>SITE</h4><ul><li>Terms of Service</li><li>Privacy Policy</li><li>Copyright Policy</li><li>Returns Policy</li><li>Support</li></ul></div>
    <div class="abs foot-col" style="left:490px"><h4>SHOP</h4><ul><li>About Us</li><li>Catalogue</li><li>Shipping Services</li><li>Shop Location</li><li>Contact Us</li></ul></div>
    <div class="abs foot-col" style="left:723px"><h4>FIND US</h4><ul><li>Wren Bay,</li><li>Saltwater Coast,</li><li>Eastland Shore</li><li>2014 © All rights reserved.</li></ul><div class="social"><i></i><i></i><i></i></div></div>
  </footer>
</div>
</body>
</html>
```